Update PowerPoint Template Font & Color

We purchased a new PowerPoint template (attached) for our organization which needs to be updated with our color palette and fonts (also attached).

Please edit the master slides to reflect our fonts and udpate the graphic elements to reflect our color scheme.

NOTE: we do not want to change the slide background color (beige) or the dark blue accent color, those colors remain in the presentation template. All fonts must be large enough to be legible for a large presentation group at a conference.

```html
<!DOCTYPE html>
<html lang="en">
<head>
<meta charset="utf-8">
<title>Foam Pack Summit 2026 – Slide Template</title>
<link rel="stylesheet" href="https://fonts.googleapis.com/css2?family=Poppins:wght@300;400;700;800&family=Barlow+Semi+Condensed:wght@600;700&display=swap">
<style>
  :root {
    --canvas: #bfbfc1;
    --navy: #10294d;
    --beige: #ebe3d9;
    --teal: #486a78;
    --cream: #e6e3b6;
    --sand: #ebe3d9;
    --white: #ffffff;
    --ink: #1d1d1d;
    --photo-a: #e6d8c8;
    --photo-b: #d9cbb8;
    --photo-c: #dcc6a8;
  }
  * { box-sizing: border-box; margin: 0; padding: 0; }
  html, body { width: 960px; height: 1200px; overflow: hidden; }
  body { background: var(--canvas); position: relative; font-family: "Poppins", sans-serif; }

  .slide { position: absolute; left: 25px; width: 910px; height: 512px; background: var(--beige); overflow: hidden; }
  .slide--title { top: 81px; }
  .slide--gallery { top: 630px; }

  .navy-band { position: absolute; left: 0; top: 0; bottom: 0; background: var(--navy); }
  .slide--title .navy-band { width: 307px; }
  .slide--gallery .navy-band { width: 200px; }

  .title-card {
    position: absolute; left: 47px; top: 93px; width: 372px; height: 326px;
    background: var(--teal);
    border-radius: 28px 64px 0 64px;
  }
  .title-card__name {
    position: absolute; left: 28px; top: 30px; width: 320px;
    font-weight: 800; color: var(--white); line-height: 1.02; letter-spacing: -1px;
  }
  .title-card__name span { display: block; }
  .title-card__line--md { font-size: 54px; }
  .title-card__line--lg { font-size: 76px; }
  .title-card__url {
    position: absolute; left: 32px; top: 268px;
    font-family: "Barlow Semi Condensed", sans-serif; font-weight: 700; font-size: 27px;
    color: var(--sand); letter-spacing: 0.3px;
  }

  .session-label { position: absolute; left: 50px; top: 421px; font-size: 29px; font-weight: 400; color: var(--white); }

  .topic-card {
    position: absolute; left: 460px; width: 402px; height: 120px;
    background: var(--teal); color: var(--white);
    border-radius: 20px 32px 0 20px;
  }
  .topic-card:nth-of-type(1) { top: 45px; }
  .topic-card:nth-of-type(2) { top: 188px; }
  .topic-card:nth-of-type(3) { top: 329px; }
  .topic-card__icon { position: absolute; left: 19px; top: 30px; width: 60px; height: 60px; }
  .topic-card__heading { position: absolute; left: 117px; top: 14px; font-family: "Barlow Semi Condensed", sans-serif; font-weight: 700; font-size: 18px; letter-spacing: 0.3px; }
  .topic-card__heading--lead { font-size: 25px; top: 16px; }
  .topic-card__text { position: absolute; left: 118px; top: 46px; width: 245px; font-size: 13px; font-weight: 300; line-height: 1.24; }
  .topic-card__text--lead { font-size: 15px; top: 52px; line-height: 1.2; width: 245px; }

  .vertical-title {
    position: absolute; left: 115px; top: 256px;
    transform: translate(-50%, -50%) rotate(-90deg);
    white-space: nowrap; color: var(--white); font-size: 28px; font-weight: 400; line-height: 1.2;
  }

  .photo { position: absolute; }
  .photo--lamp { left: 243px; top: 32px; width: 196px; height: 375px; background: linear-gradient(160deg, #ece2d6, var(--photo-a) 55%, #d8c9b6); }
  .photo--lobby { left: 452px; top: 32px; width: 196px; height: 181px; background: linear-gradient(180deg, #c9a07d 0%, #e8ddd2 50%, #a9a9ab 100%); }
  .photo--vase { left: 452px; top: 225px; width: 196px; height: 182px; background: linear-gradient(135deg, #f1e4d0, var(--photo-c) 70%, #caa57d); }
  .photo--concrete { left: 660px; top: 32px; width: 196px; height: 375px; background: linear-gradient(180deg, #e9d8c2, var(--photo-b) 70%, #c9b29a); }

  .gallery-caption { position: absolute; left: 248px; top: 434px; width: 592px; font-size: 13px; line-height: 1.25; color: var(--ink); }
</style>
</head>
<body>

<section class="slide slide--title">
  <div class="navy-band"></div>

  <div class="title-card">
    <h1 class="title-card__name">
      <span class="title-card__line--md">FOAM PACK</span>
      <span class="title-card__line--lg">SUMMIT</span>
      <span class="title-card__line--md">2026</span>
    </h1>
    <span class="title-card__url">www.foampacksummit.org</span>
  </div>

  <p class="session-label">General Session</p>

  <article class="topic-card">
    <svg class="topic-card__icon" viewBox="0 0 60 60" fill="none" stroke="#fff" stroke-width="1.6" stroke-linejoin="round" aria-hidden="true">
      <path d="M10 10l1.8 3.6 4 .6-2.9 2.8.7 4-3.6-1.9-3.6 1.9.7-4-2.9-2.8 4-.6z"/>
      <path d="M30 4l1.8 3.6 4 .6-2.9 2.8.7 4-3.6-1.9-3.6 1.9.7-4-2.9-2.8 4-.6z"/>
      <path d="M50 10l1.8 3.6 4 .6-2.9 2.8.7 4-3.6-1.9-3.6 1.9.7-4-2.9-2.8 4-.6z"/>
      <circle cx="30" cy="36" r="14"/>
      <circle cx="30" cy="32" r="4.5"/>
      <path d="M21 46c2-5 5.5-7 9-7s7 2 9 7"/>
      <circle cx="44" cy="48" r="7" fill="#486a78"/>
      <path d="M40.5 48l2.5 2.5 4.5-4.5"/>
    </svg>
    <h2 class="topic-card__heading topic-card__heading--lead">EPR Outlook For EPS</h2>
    <p class="topic-card__text topic-card__text--lead">See how EPS transport packaging is positioned within different EPR laws.</p>
  </article>

  <article class="topic-card">
    <svg class="topic-card__icon" viewBox="0 0 60 60" fill="none" stroke="#fff" stroke-width="1.6" stroke-linejoin="round" aria-hidden="true">
      <path d="M30 4l4 3.5 5.2-.8 2 4.8 4.8 2-.8 5.2 3.5 4-3.5 4 .8 5.2-4.8 2-2 4.8-5.2-.8-4 3.5-4-3.5-5.2.8-2-4.8-4.8-2 .8-5.2-3.5-4 3.5-4-.8-5.2 4.8-2 2-4.8 5.2.8z"/>
      <circle cx="30" cy="22.5" r="9"/>
      <path d="M25.5 22.5l3 3 6-6"/>
      <path d="M20 38l-8 15 6-1.5 3 5.5 7-14"/>
      <path d="M40 38l8 15-6-1.5-3 5.5-7-14"/>
    </svg>
    <h2 class="topic-card__heading">Lorem Ipsum Dolor</h2>
    <p class="topic-card__text">Lorem ipsum dolor sit amet, consectetur adipiscing elit, sed eiusmod tempor incididunt ut labore et dolore magna aliqua.</p>
  </article>

  <article class="topic-card">
    <svg class="topic-card__icon" viewBox="0 0 60 60" fill="none" stroke="#fff" stroke-width="1.6" stroke-linejoin="round" stroke-linecap="round" aria-hidden="true">
      <path d="M20 56V46c-5-4-8-9-8-16 0-12 9-22 21-22s20 9 20 20c0 3-1 5-1 5l4 7-5 2v6c0 3-2 4-5 4h-5v4"/>
      <circle cx="32" cy="28" r="11"/>
      <path d="M28.5 25c0-2.5 1.5-4 3.5-4s3.5 1.5 3.5 3.5c0 3-3.5 3-3.5 6"/>
      <circle cx="32" cy="34" r="0.6" fill="#fff"/>
    </svg>
    <h2 class="topic-card__heading">Lorem Ipsum Dolor</h2>
    <p class="topic-card__text">Lorem ipsum dolor sit amet, consectetur adipiscing elit, sed eiusmod tempor incididunt ut labore et dolore magna aliqua.</p>
  </article>
</section>

<section class="slide slide--gallery">
  <div class="navy-band"></div>
  <p class="vertical-title">Your Business<br>Presentation</p>

  <div class="photo photo--lamp" role="img" aria-label="Photo: beige room corner with a white floor lamp, wall lamp and wall clock"></div>
  <div class="photo photo--lobby" role="img" aria-label="Photo: modern lobby with wooden slat wall, stone bench and grey carpet"></div>
  <div class="photo photo--vase" role="img" aria-label="Photo: sunlit shelf with a tan vase, dried leaf and stacked books"></div>
  <div class="photo photo--concrete" role="img" aria-label="Photo: warm-toned concrete column and stairway detail"></div>

  <p class="gallery-caption">Lorem ipsum dolor sit amet, consectetur adipiscing elit, sed do eiusmod tempor incididunt ut labore et dolore magna aliqua. Ut enim ad minim veniam.</p>
</section>

</body>
</html>
```